ZOR Clinic

We are a telemedicine based HIV treatment, prevention and hep c clinic looking to help make our online presence known.

Target Market(s)

Future patients. We want to this be informative and have stock images of all different types of people

Industry/Entity Type

Medical

Coding

Coded - Design and coding required

Requirements
Must have
• A Home Page, A page on PrEP, HIV treatment and Hep C. A box in the corner that says book now and a contact us page.

```html
<!DOCTYPE html>
<html lang="en">
<head>
<meta charset="UTF-8">
<title>ZOR Clinic – Confidential Online HIV &amp; Hepatitis C Care</title>
<link href="https://fonts.googleapis.com/css2?family=Poppins:ital,wght@0,400;0,500;0,600;0,700;1,400&display=swap" rel="stylesheet">
<style>
:root{
  --blue:#1aa6dc;
  --blue-deep:#3a93c6;
  --ink:#222a30;
  --text:#3a4249;
  --muted:#5a636b;
  --white:#ffffff;
  --pale:#eef6fb;
  --line:#dde6ec;
  --star:#f5c518;
}
*{box-sizing:border-box;margin:0;padding:0}
html,body{width:1200px;height:4119px;overflow:hidden}
body{font-family:'Poppins',sans-serif;color:var(--text);background:linear-gradient(180deg,#ffffff 0%,var(--pale) 100%);position:relative}
.abs{position:absolute}
.btn{position:absolute;display:flex;align-items:center;justify-content:center;font-size:15px;border-radius:4px;text-decoration:none}
.btn-solid{background:linear-gradient(180deg,var(--blue),var(--blue-deep));color:var(--white)}
.btn-ghost{border:1.5px solid #555;color:var(--ink);background:var(--white)}
.btn-outline-light{border:1.5px solid rgba(255,255,255,.85);color:var(--white)}
.accent{color:var(--blue)}
.ph{position:absolute;overflow:hidden}

/* header */
.site-header{position:absolute;left:0;top:0;width:1200px;height:96px;background:var(--white);border-bottom:1px solid var(--line)}
.brand{position:absolute;display:flex;align-items:center;gap:10px;font-weight:600;color:var(--ink)}
.brand-dot{width:34px;height:34px;border-radius:50%;background:var(--blue)}
.nav a{position:absolute;top:28px;font-size:16px;color:var(--ink);text-decoration:none}

/* hero */
.hero-title{position:absolute;left:113px;top:186px;font-size:51px;line-height:61px;font-weight:700;color:var(--ink)}
.hero-text{position:absolute;left:113px;top:330px;width:460px;font-size:17px;line-height:29px;color:var(--ink)}

/* steps */
.steps{position:absolute;left:0;top:636px;width:1200px;height:586px;background:linear-gradient(180deg,var(--blue) 0%,var(--blue-deep) 100%)}
.section-title{position:absolute;width:1200px;text-align:center;font-size:40px;font-weight:700;color:var(--ink)}
.steps .section-title{color:var(--white);top:76px}
.step{position:absolute;top:196px;width:182px;padding-top:32px;color:var(--white)}
.step.active{width:259px;height:291px;padding:32px 40px 32px 47px;background:var(--white);color:var(--text);border-radius:16px;box-shadow:0 10px 30px rgba(0,0,0,.12)}
.step-icon{width:73px;height:73px;border-radius:50%;background:var(--white);display:flex;align-items:center;justify-content:center}
.step.active .step-icon{background:var(--blue)}
.step h3{margin-top:26px;font-size:17px;line-height:23px;font-weight:600}
.step.active h3{color:var(--ink)}
.step p{margin-top:12px;font-size:13.5px;line-height:22px}

/* services */
.tab{position:absolute;left:136px;font-size:18px;font-weight:600;color:var(--ink)}
.tab.current{background:linear-gradient(180deg,var(--blue),var(--blue-deep));color:var(--white);width:174px;height:49px;border-radius:6px;padding-left:34px;display:flex;align-items:center}
.tab.plain{left:170px}
.service-card{position:absolute;left:350px;top:1441px;width:741px;height:264px;background:var(--white);border-radius:16px;overflow:hidden;box-shadow:0 8px 30px rgba(20,80,120,.08)}

/* testimonials */
.thumb{position:absolute;left:113px;width:219px;border-radius:16px;overflow:hidden}
.quote-card{position:absolute;left:364px;top:1954px;width:727px;height:440px;border-radius:20px;background:linear-gradient(180deg,var(--blue),var(--blue-deep));color:var(--white);padding:46px 44px 40px 48px}
.quote-main{font-size:27px;line-height:44px;font-style:italic;font-weight:400}
.quote-small{margin-top:14px;font-size:15px;line-height:27px}
.quote-name{margin-top:20px;font-size:20px;font-weight:600;line-height:28px}
.stars{display:block;margin-top:8px}

/* partner */
.feature{position:absolute;width:230px;height:233px;background:var(--white);border-radius:16px;padding:30px 20px 30px 33px;box-shadow:0 8px 26px rgba(20,80,120,.08)}
.feature.highlight{background:linear-gradient(180deg,var(--blue),var(--blue-deep));color:var(--white)}
.feature h4{font-size:16.5px;line-height:25px;font-weight:600;color:var(--ink)}
.feature.highlight h4{color:var(--white)}
.feature p{margin-top:10px;font-size:13px;line-height:22px}

/* cta */
.cta{position:absolute;left:0;top:3175px;width:1200px;height:512px;background:linear-gradient(180deg,var(--blue),var(--blue-deep))}

/* footer */
.copyright{position:absolute;left:0;top:4064px;width:1200px;height:55px;background:linear-gradient(180deg,var(--blue),var(--blue-deep));color:var(--white);font-size:13px;display:flex;align-items:center;justify-content:center}
</style>
</head>
<body>

<header class="site-header">
  <div class="brand" style="left:117px;top:28px;font-size:20px"><span class="brand-dot"></span>ZOR Clinic</div>
  <nav class="nav">
    <a href="#" style="left:404px">Home</a>
    <a href="#" style="left:496px">PrEP</a>
    <a href="#" style="left:573px">HIV Treatment</a>
    <a href="#" style="left:729px">Hep C</a>
    <a href="#" style="left:822px">Contact Us</a>
  </nav>
  <a href="#" class="btn btn-solid" style="left:946px;top:16px;width:136px;height:48px">Book Now</a>
</header>

<section class="hero">
  <h1 class="hero-title">Confidential Online<br><span class="accent">HIV &amp; Hepatitis C Care</span></h1>
  <p class="hero-text">Fast, private telemedicine appointments for HIV treatment, PrEP, and Hepatitis C care—all from the comfort of your home.</p>
  <a href="#" class="btn btn-solid" style="left:113px;top:444px;width:211px;height:50px">Book Appointment</a>
  <a href="#" class="btn btn-ghost" style="left:339px;top:444px;width:154px;height:50px">Learn More</a>
  <div class="ph" role="img" aria-label="Smiling healthcare provider in scrubs on a video call at a laptop" style="left:596px;top:141px;width:604px;height:418px">
    <div class="abs" style="left:152px;top:6px;width:342px;height:342px;border-radius:171px 171px 0 0;background:var(--blue)"></div>
    <div class="abs" style="left:0;top:300px;width:604px;height:118px;background:linear-gradient(180deg,#c9d3da,#9ea9b1)"></div>
    <div class="abs" style="left:210px;top:60px;width:230px;height:300px;border-radius:110px 110px 20px 20px;background:linear-gradient(180deg,#6aa5cf,#8cbcdf)"></div>
  </div>
</section>

<section class="steps">
  <h2 class="section-title">How It Works</h2>
  <div class="step" style="left:113px">
    <div class="step-icon"><svg width="34" height="34" viewBox="0 0 24 24" fill="var(--blue)"><circle cx="12" cy="7" r="4"/><rect x="5" y="13" width="14" height="9" rx="2"/></svg></div>
    <h3>Book Online</h3>
    <p>Choose a convenient appointment time through our secure online booking system.</p>
  </div>
  <div class="step active" style="left:332px">
    <div class="step-icon"><svg width="34" height="34" viewBox="0 0 24 24" fill="#fff"><circle cx="9" cy="7" r="3.5"/><path d="M3 21v-4a6 6 0 0 1 12 0v4z"/><circle cx="18" cy="6" r="4" fill="none" stroke="#fff" stroke-width="1.6"/><path d="M18 4v4M16 6h4" stroke="#fff" stroke-width="1.6"/></svg></div>
    <h3>Meet Your Provider</h3>
    <p>Connect with an experienced healthcare provider via a private video consultation.</p>
  </div>
  <div class="step" style="left:644px">
    <div class="step-icon"><svg width="34" height="34" viewBox="0 0 24 24" fill="var(--blue)"><rect x="4" y="6" width="16" height="15" rx="2"/><rect x="8" y="2" width="2" height="6"/><path d="M8 13l3 3 5-5" stroke="#fff" stroke-width="2" fill="none"/></svg></div>
    <h3>Receive Your<br>Treatment Plan</h3>
    <p>Get a personalized care plan, prescriptions (if appropriate), and expert guidance.</p>
  </div>
  <div class="step" style="left:909px">
    <div class="step-icon"><svg width="34" height="34" viewBox="0 0 24 24" fill="var(--blue)"><circle cx="12" cy="8" r="4"/><path d="M4 21a8 8 0 0 1 16 0z"/><path d="M6 8a6 6 0 0 1 12 0" stroke="var(--blue)" stroke-width="1.6" fill="none"/></svg></div>
    <h3>Ongoing Support</h3>
    <p>Receive follow-up care, medication management, and continued support whenever you need it.</p>
  </div>
</section>

<section class="services">
  <h2 class="section-title" style="top:1330px">Our Core <span class="accent">Services</span></h2>
  <div class="tab current" style="top:1440px">PrEP</div>
  <div class="abs" style="left:320px;top:1444px;width:4px;height:40px;background:var(--blue)"></div>
  <div class="tab plain" style="top:1518px">HIV Treatment</div>
  <div class="tab plain" style="top:1579px">Hepatitis C</div>
  <div class="service-card">
    <div class="ph" role="img" aria-label="Patient resting in bed during a video consultation with a doctor on a laptop" style="left:0;top:0;width:380px;height:264px;background:linear-gradient(135deg,#b8c2cc 0%,#6c7fa8 55%,#3d4f8c 100%)"></div>
    <div class="abs" style="left:420px;top:48px;width:290px">
      <h3 style="font-size:16px;font-weight:600;color:var(--ink)">PrEP</h3>
      <p style="margin-top:18px;font-size:14px;line-height:22px">Stay protected with confidential online PrEP consultations, prescriptions, and ongoing support.</p>
    </div>
    <a href="#" class="btn btn-solid" style="left:420px;top:170px;width:139px;height:49px">Learn More</a>
  </div>
</section>

<section class="testimonials">
  <h2 class="section-title" style="top:1850px">Trusted by Our <span class="accent">Patients</span></h2>
  <div class="thumb" role="img" aria-label="Person on a video call with a doctor on a laptop" style="top:1954px;height:99px;background:linear-gradient(135deg,#8a7a6c,#d9dde2)"></div>
  <div class="thumb" role="img" aria-label="Smiling older patient portrait" style="top:2063px;height:221px;border:3px solid var(--blue);background:linear-gradient(180deg,#cfd3d6,#9aa0a6)"></div>
  <div class="thumb" role="img" aria-label="Patient in a video consultation at home" style="top:2295px;height:99px;background:linear-gradient(135deg,#6b4d3c,#e3e0da)"></div>
  <div class="quote-card">
    <p class="quote-main">"The entire process was simple, private, and professional. I was able to speak with a caring provider from home and received my treatment plan quickly. Highly recommend ZOR Clinic."</p>
    <p class="quote-small">"The entire process was simple, private, and professional. I was able to speak with a caring provider from home and received my treatment plan quickly.</p>
    <p class="quote-name">Dana R.</p>
    <svg class="stars" width="106" height="18" viewBox="0 0 106 18" fill="var(--star)">
      <g id="star"><polygon points="9,0 11.6,6 18,6.5 13,10.7 14.6,17 9,13.6 3.4,17 5,10.7 0,6.5 6.4,6"/></g>
      <use href="#star" x="22"/><use href="#star" x="44"/><use href="#star" x="66"/><use href="#star" x="88"/>
    </svg>
  </div>
</section>

<section class="partner">
  <h2 class="abs" style="left:115px;top:2538px;font-size:40px;line-height:51px;font-weight:700;color:var(--ink)">Your Trusted Partner<br>in <span class="accent">Online Healthcare</span></h2>
  <p class="abs" style="left:115px;top:2668px;width:395px;font-size:17px;line-height:29px">Quality healthcare that's private, convenient, and tailored to your needs. Our experienced team is committed to providing compassionate online care you can trust.</p>
  <p class="abs" style="left:115px;top:2830px;width:405px;font-size:17px;line-height:29px">Our secure telehealth services make accessing HIV treatment, PrEP, and Hepatitis C care simple, convenient, and personalized to your needs.</p>
  <a href="#" class="btn btn-solid" style="left:115px;top:2982px;width:211px;height:48px">Book Appointment</a>
  <div class="feature highlight" style="left:612px;top:2544px">
    <h4>Private and<br>Confidential</h4>
    <p>Your consultations and medical information are handled with the highest level of privacy and security.</p>
    <svg class="abs" style="right:20px;bottom:16px;opacity:.5" width="36" height="36" viewBox="0 0 24 24" fill="#fff"><path d="M12 2l8 3v6c0 5-3.5 9-8 11-4.5-2-8-6-8-11V5z"/></svg>
  </div>
  <div class="feature" style="left:865px;top:2544px">
    <h4>Convenient<br>Telehealth</h4>
    <p>Access expert care from the comfort of your home with secure online appointments.</p>
  </div>
  <div class="feature" style="left:612px;top:2800px">
    <h4 style="white-space:nowrap">Experienced<br>Healthcare Providers</h4>
    <p>Receive personalized care from qualified professionals experienced in HIV and Hepatitis C treatment.</p>
  </div>
  <div class="feature" style="left:865px;top:2800px">
    <h4 style="white-space:nowrap">Fast &amp; Personalized<br>Care</h4>
    <p>Book quickly, receive timely treatment plans, and enjoy ongoing support tailored to your health needs.</p>
  </div>
</section>

<section class="cta">
  <div class="ph" role="img" aria-label="Smiling doctor with glasses and stethoscope talking on a laptop video call" style="left:113px;top:75px;width:478px;height:338px;border-radius:16px;background:linear-gradient(135deg,#e8ebee 0%,#c8ccd0 50%,#7c8a96 100%)"></div>
  <h2 class="abs" style="left:668px;top:80px;font-size:40px;line-height:51px;font-weight:700;color:var(--white)">Take Control of Your<br>Health Today</h2>
  <p class="abs" style="left:668px;top:195px;width:395px;font-size:17px;line-height:29px;color:var(--white)">Quality healthcare that's private, convenient, and tailored to your needs. Our experienced team is committed to providing compassionate online care you can trust.</p>
  <a href="#" class="btn btn-outline-light" style="left:668px;top:360px;width:145px;height:50px">Book Now</a>
</section>

<footer>
  <div class="brand" style="left:113px;top:3818px;font-size:26px"><span class="brand-dot" style="width:44px;height:44px"></span>ZOR Clinic</div>
  <a href="#" class="btn btn-solid" style="left:879px;top:3810px;width:211px;height:48px">Book Appointment</a>
  <p class="abs" style="left:113px;top:3912px;width:980px;font-size:17px;line-height:29px">Providing confidential, compassionate, and convenient telehealth services for HIV treatment, PrEP, and Hepatitis C care. Access expert care from the comfort of your home.</p>
  <div class="copyright">© 2026 ZOR Clinic. All Rights Reserved.</div>
</footer>

</body>
</html>
```